Redesign of the iOS/apk app vorbu.

I have an app that need a new more vibrant modern design, I already have a draft in jpg but I need it in psd and some minor animation very simple.

We also need a high high end design(r) for Kxxxx Bxx, play with the D and S, think Maren Trovelle, Pavone, Tormi, Odile Brancart Nemours and so on. Also need pattern and more. it needs to work as small, big letters, signs, clothes, sunglasses, coffee cups, plates, basically on everything.

Sunglasses

```html
<!DOCTYPE html>
<html lang="en">
<head>
<meta charset="utf-8">
<title>Vorbu – game screens</title>
<link rel="stylesheet" href="https://fonts.googleapis.com/css2?family=Arimo:wght@400;700&family=Ubuntu:wght@500&display=swap">
<style>
  :root {
    --bg: #ffffff;
    --status-bg: #000000;
    --status-text: #ffffff;
    --header-top: #e7a863;
    --header-bottom: #d08c45;
    --header-btn: #dca064;
    --header-btn-edge: #a86a2c;
    --square-light: #f0dbbb;
    --square-dark: #8e3a1a;
    --panel: #dcbf94;
    --panel-edge: #b89a6c;
    --tile-crimson: #9c0a3c;
    --tile-teal: #07a3ba;
    --tile-blue: #2232e4;
    --pass: #d41fb4;
    --surrender: #e8721a;
    --roll: #1e7d12;
    --piece-white: #ffffff;
    --piece-black: #111111;
  }
  * { box-sizing: border-box; margin: 0; padding: 0; }
  html, body { width: 1200px; height: 1183px; overflow: hidden; background: var(--bg); }
  body { position: relative; font-family: "Arimo", Arial, sans-serif; }

  .screen {
    position: absolute; top: 172px; width: 416px; height: 734px;
    background: var(--panel); overflow: hidden;
  }
  .screen--left { left: 72px; }
  .screen--right { left: 615px; }

  .status-bar {
    height: 28px; background: var(--status-bg); color: var(--status-text);
    font-size: 16px; display: flex; align-items: center; justify-content: space-between;
    padding: 0 6px 0 0;
  }
  .status-bar__left { display: flex; align-items: center; gap: 8px; }
  .status-bar__vpn { font-size: 10px; font-weight: 700; border: 1px solid #fff; padding: 0 2px; line-height: 12px; }
  .status-bar__time { position: absolute; left: 50%; transform: translateX(-50%); }
  .status-bar__right { display: flex; align-items: center; gap: 6px; }

  .app-header {
    height: 48px; position: relative;
    background: linear-gradient(var(--header-top), var(--header-bottom));
    border-bottom: 2px solid #f3e2c6;
    display: flex; align-items: center; justify-content: space-between; padding: 0 14px;
  }
  .app-header__btn {
    font-family: "Ubuntu", sans-serif; font-size: 14px; color: #fff;
    width: 84px; height: 30px; border-radius: 6px;
    background: var(--header-btn); border: 1px solid var(--header-btn-edge);
    box-shadow: inset 0 1px 0 rgba(255,255,255,.4);
    display: flex; align-items: center; justify-content: center;
  }
  .app-header__title {
    position: absolute; left: 50%; transform: translateX(-50%);
    color: #fff; font-size: 23px;
  }

  .board {
    width: 416px; height: 416px;
    background: repeating-conic-gradient(var(--square-dark) 0 25%, var(--square-light) 0 50%) 0 0 / 104px 104px;
    display: grid; grid-template: repeat(8, 52px) / repeat(8, 52px);
  }
  .piece {
    display: flex; align-items: center; justify-content: center;
    font-family: "DejaVu Sans", "Segoe UI Symbol", sans-serif; font-size: 38px; line-height: 1;
  }
  .piece--white { color: var(--piece-white); text-shadow: 0 0 1px #555, 1px 2px 2px rgba(0,0,0,.5); }
  .piece--black { color: var(--piece-black); text-shadow: 1px 2px 2px rgba(0,0,0,.3); }

  .dice-tray {
    position: absolute; left: 8px; top: 510px; width: 398px; height: 130px;
    border: 2px solid var(--panel-edge); border-radius: 8px;
  }
  .die {
    position: absolute; top: 22px; width: 96px; height: 86px; border-radius: 4px;
    display: flex; align-items: center; justify-content: center;
    font-family: "DejaVu Sans", "Segoe UI Symbol", sans-serif; font-size: 66px; color: #fff;
    text-shadow: 2px 3px 3px rgba(0,0,0,.5);
    box-shadow: 0 2px 3px rgba(0,0,0,.35), inset 0 0 0 2px rgba(0,0,0,.15);
  }
  .die--1 { left: 15px; } .die--2 { left: 160px; } .die--3 { left: 288px; }
  .die--crimson { background: var(--tile-crimson); }
  .die--teal { background: var(--tile-teal); }
  .die--blue { background: var(--tile-blue); }

  .actions { position: absolute; top: 660px; left: 3px; width: 410px; height: 44px; }
  .action {
    position: absolute; top: 0; height: 44px; border-radius: 5px;
    color: #fff; font-size: 21px; display: flex; align-items: center; justify-content: center;
    box-shadow: 0 2px 2px rgba(0,0,0,.3), inset 0 1px 0 rgba(255,255,255,.35);
  }
  .action--pass { left: 0; width: 131px; background: linear-gradient(#e553cf, var(--pass)); }
  .action--surrender { left: 139px; width: 131px; background: linear-gradient(#f59a44, var(--surrender)); }
  .action--roll { left: 277px; width: 132px; background: linear-gradient(#2e9a20, var(--roll)); }
</style>
</head>
<body>

<section class="screen screen--left">
  <div class="status-bar">
    <div class="status-bar__left"><span>No Service</span><span class="status-bar__vpn">VPN</span></div>
    <span class="status-bar__time">16:20</span>
    <div class="status-bar__right"><span>100%</span>
      <svg width="22" height="11" viewBox="0 0 22 11"><rect x="0.5" y="0.5" width="19" height="10" fill="none" stroke="#fff"/><rect x="2" y="2" width="16" height="7" fill="#fff"/><rect x="20" y="3.5" width="2" height="4" fill="#fff"/></svg>
    </div>
  </div>
  <header class="app-header">
    <span class="app-header__btn">Rules</span>
    <h1 class="app-header__title">Vorbu</h1>
    <span class="app-header__btn">Status</span>
  </header>
  <div class="board">
    <span class="piece piece--white" style="grid-area:1/1">♜</span>
    <span class="piece piece--white" style="grid-area:1/3">♛</span>
    <span class="piece piece--white" style="grid-area:2/5">♞</span>
    <span class="piece piece--white" style="grid-area:3/2">♜</span>
    <span class="piece piece--white" style="grid-area:3/4">♟</span>
    <span class="piece piece--black" style="grid-area:6/6">♛</span>
    <span class="piece piece--black" style="grid-area:7/2">♜</span>
    <span class="piece piece--black" style="grid-area:7/5">♟</span>
    <span class="piece piece--black" style="grid-area:8/3">♞</span>
    <span class="piece piece--black" style="grid-area:8/8">♜</span>
  </div>
  <div class="dice-tray">
    <span class="die die--1 die--crimson">♜</span>
    <span class="die die--2 die--crimson">♛</span>
    <span class="die die--3 die--crimson">♞</span>
  </div>
  <nav class="actions">
    <span class="action action--pass">Pass</span>
    <span class="action action--surrender">Surrender</span>
    <span class="action action--roll">Roll Dice</span>
  </nav>
</section>

<section class="screen screen--right">
  <div class="status-bar">
    <div class="status-bar__left"><span>No Service</span><span class="status-bar__vpn">VPN</span></div>
    <span class="status-bar__time">16:20</span>
    <div class="status-bar__right"><span>100%</span>
      <svg width="22" height="11" viewBox="0 0 22 11"><rect x="0.5" y="0.5" width="19" height="10" fill="none" stroke="#fff"/><rect x="2" y="2" width="16" height="7" fill="#fff"/><rect x="20" y="3.5" width="2" height="4" fill="#fff"/></svg>
    </div>
  </div>
  <header class="app-header">
    <span class="app-header__btn">Rules</span>
    <h1 class="app-header__title">Vorbu</h1>
    <span class="app-header__btn">Status</span>
  </header>
  <div class="board">
    <span class="piece piece--white" style="grid-area:1/1">♜</span>
    <span class="piece piece--white" style="grid-area:1/3">♛</span>
    <span class="piece piece--white" style="grid-area:2/5">♞</span>
    <span class="piece piece--white" style="grid-area:3/2">♜</span>
    <span class="piece piece--white" style="grid-area:3/4">♟</span>
    <span class="piece piece--black" style="grid-area:6/6">♛</span>
    <span class="piece piece--black" style="grid-area:7/2">♜</span>
    <span class="piece piece--black" style="grid-area:7/5">♟</span>
    <span class="piece piece--black" style="grid-area:8/3">♞</span>
    <span class="piece piece--black" style="grid-area:8/8">♜</span>
  </div>
  <div class="dice-tray">
    <span class="die die--1 die--teal">♜</span>
    <span class="die die--2 die--blue">♛</span>
    <span class="die die--3 die--blue">♞</span>
  </div>
  <nav class="actions">
    <span class="action action--pass">Pass</span>
    <span class="action action--surrender">Surrender</span>
    <span class="action action--roll">Roll Dice</span>
  </nav>
</section>

</body>
</html>
```